Quorvane - corporate Business Card

We need a good look and innovative business card for a new start up company based in Los Angeles called "Quorvane". We are in a payment business, including payment card, app, and ewallet. We are expert in online payment and Card not present (CNP) transaction.
We need an innovative, modern business card.

Our logo font is Aero Matics

Target Market(s)

Startup - Bank - Online Payment - Card Manufacturing

Industry/Entity Type

Startup

Contact Information for Business Card

phone: 424 555 0173 - Address: 4270 Marbrook blvd, Dunhaven City, CA 90418

Requirements
Must have
• Message: innovative, professional, expert, high tech, trust, online payment expert, security
Nice to have
• no comment
Should not have
• no Comment

```html
<!DOCTYPE html>
<html lang="en">
<head>
<meta charset="utf-8">
<title>Quorvane — Business Card</title>
<link rel="stylesheet" href="https://fonts.googleapis.com/css2?family=Open+Sans:wght@400;600&display=swap">
<style>
  :root {
    --brand-red: #b81f31;
    --brand-pale: #f5dfe2;
    --stripe-grey: #8a8a8a;
    --card-white: #ffffff;
    --ink-grey: #555555;
    --backdrop: #ecebe8;
  }
  * { box-sizing: border-box; margin: 0; padding: 0; }
  html, body {
    width: 1200px; height: 987px; overflow: hidden;
    background: var(--backdrop);
    font-family: "Open Sans", Arial, sans-serif;
  }
  .canvas { position: relative; width: 1200px; height: 987px; }
  .card {
    position: absolute; left: 292px; width: 616px; height: 351px;
    background: var(--card-white);
    box-shadow: 0 2px 8px rgba(0,0,0,0.18);
    overflow: hidden;
  }
  .card--front { top: 130px; }
  .card--back { top: 505px; }
  .card__art { position: absolute; inset: 0; }

  .brand {
    position: absolute; display: flex; align-items: center;
    color: var(--brand-red); font-weight: 600;
  }
  .brand--front { left: 39px; top: 48px; gap: 12px; font-size: 50px; line-height: 1; }
  .brand__dot { width: 76px; height: 76px; border-radius: 50%; background: var(--brand-red); flex: none; }

  .contact { position: absolute; left: 41px; top: 249px; list-style: none; color: #fff; font-size: 16px; }
  .contact li { display: flex; align-items: center; gap: 9px; height: 23.5px; }
  .contact svg { width: 14px; height: 14px; fill: #fff; flex: none; }

  .person { position: absolute; right: 38px; top: 212px; text-align: right; color: #fff; }
  .person__name { font-size: 21px; font-weight: 600; line-height: 1.25; }
  .person__role { margin-top: 2px; font-size: 16px; line-height: 1.3; }
  .person__address { margin-top: 14px; font-size: 16px; line-height: 23.5px; font-style: normal; }

  .back__circle {
    position: absolute; left: 16px; top: 17px; width: 318px; height: 318px;
    border-radius: 50%; background: var(--brand-pale);
  }
  .brand--back { right: 40px; top: 248px; font-size: 54px; line-height: 1; }
  .back__web {
    position: absolute; right: 38px; top: 310px;
    font-size: 14px; letter-spacing: 4.5px; color: var(--ink-grey);
  }
</style>
</head>
<body>
<main class="canvas">
  <section class="card card--front" aria-label="Business card front">
    <svg class="card__art" viewBox="0 0 616 351" aria-hidden="true">
      <polygon points="0,189 352,189 340,202 0,202" fill="var(--stripe-grey)"/>
      <polygon points="356,177 616,177 616,351 0,351 0,206 333,206" fill="var(--brand-red)"/>
    </svg>
    <div class="brand brand--front"><span class="brand__dot"></span>Quorvane</div>

    <ul class="contact">
      <li><svg viewBox="0 0 24 24"><path d="M6.6 10.8a15.2 15.2 0 0 0 6.6 6.6l2.2-2.2c.3-.3.7-.4 1-.2 1.1.4 2.3.6 3.6.6.6 0 1 .4 1 1V20c0 .6-.4 1-1 1A17 17 0 0 1 3 4c0-.6.4-1 1-1h3.5c.6 0 1 .4 1 1 0 1.3.2 2.5.6 3.6.1.3 0 .7-.2 1z"/></svg>424 555 0173</li>
      <li><svg viewBox="0 0 24 24"><path d="M2 5h20v14H2z M3.5 6.5 12 13l8.5-6.5" fill="none" stroke="#fff" stroke-width="2"/></svg>marcus@quorvane.com</li>
      <li><svg viewBox="0 0 24 24"><circle cx="12" cy="12" r="10"/><path d="M8 6c2 1 3 3 2 5s-3 2-3 4M15 5c-1 2 0 3 2 4s2 4 1 6" fill="none" stroke="var(--brand-red)" stroke-width="2"/></svg>www.quorvane.com</li>
    </ul>

    <div class="person">
      <p class="person__name">MARCUS HALE</p>
      <p class="person__role">CEO&amp;Founder</p>
      <address class="person__address">4270 Marbrook blvd<br>Dunhaven City, CA 90418</address>
    </div>
  </section>

  <section class="card card--back" aria-label="Business card back">
    <div class="back__circle"></div>
    <div class="brand brand--back">Quorvane</div>
    <p class="back__web">www.quorvane.com</p>
  </section>
</main>
</body>
</html>
```